Webdesign für Bau von Wohnanlagen aus Containermodulen
Zielgruppe
Wir bauen Wohnanlagen, Bürogebäude, Kindergärten, Schulen etc. aus einzelnen Containermodulen - übernehmen die Montage, Umbau und Versetzung, Reparaturen und Einlagerungen. Unsere Zielgruppe sind überwiegend Firmen und Kommunen. Der Text für die Homepage ist bereits fertig. Hier erhalten Sie weitere Informationen über unser Tätigkeitsfeld.
Aufgabenstellung
Die Farbe unseres Logos ist blau. Sie sollte sich natürlich in der Homepage minimal widerspiegeln, aber nicht dominieren. Bilder sollten nicht zu klein gehalten werden. Wir möchten dadurch zeigen, was möglich ist (z.B. Umsetzungen von ganzen Containeranlagen am Stück - hier haben wir eine Monopolstellung).

```html
<!DOCTYPE html>
<html lang="de">
<head>
<meta charset="utf-8">
<title>KERN Montagearbeiten</title>
<link href="https://fonts.googleapis.com/css2?family=Open+Sans:wght@400;600;700&family=Roboto+Slab:wght@300&display=swap" rel="stylesheet">
<style>
  :root {
    --brand-blue: #13259b;
    --text-dark: #333333;
    --nav-text: #444444;
    --footer-bg: #5e5e5c;
    --white: #ffffff;
    --sky: #a9c4e6;
    --facade: #d9dcdc;
    --foliage: #5f7a3a;
    --ground: #8d8c86;
  }
  * { margin: 0; padding: 0; box-sizing: border-box; }
  html, body { width: 1200px; height: 1043px; overflow: hidden; background: var(--white); }
  body { font-family: "Open Sans", sans-serif; color: var(--text-dark); position: relative; }

  .site-header { position: absolute; left: 0; top: 0; width: 1200px; height: 94px; }
  .brand { position: absolute; left: 232px; top: 18px; width: 170px; height: 64px;
    display: flex; align-items: center; gap: 8px; }
  .brand-mark { width: 14px; height: 14px; background: var(--brand-blue); }
  .brand-name { font-weight: 700; font-size: 20px; color: var(--brand-blue); letter-spacing: 0.5px; }
  .tagline { position: absolute; left: 420px; top: 13px; font-family: "Roboto Slab", serif;
    font-weight: 300; font-size: 16px; color: #555; }
  .main-nav { position: absolute; top: 71px; left: 515px; font-size: 10.5px; color: var(--nav-text); }
  .main-nav a { position: absolute; white-space: nowrap; text-decoration: none; color: inherit; }
  .main-nav a.active { color: var(--brand-blue); font-weight: 700; }

  .hero { position: absolute; left: 0; top: 94px; width: 1200px; height: 495px; }
  .hero-photo { position: absolute; inset: 0;
    background: linear-gradient(180deg, var(--sky) 0%, #c9d7e6 22%, var(--facade) 45%, #c5c8c8 72%, var(--ground) 100%); }
  .hero-photo::after { content: ""; position: absolute; right: 0; top: 0; width: 260px; height: 330px;
    background: linear-gradient(90deg, rgba(95,122,58,0) 0%, rgba(95,122,58,0.75) 60%); }
  .hero-caption { position: absolute; left: 0; top: 252px; width: 528px; height: 107px;
    background: rgba(255,255,255,0.78); padding: 22px 0 0 40px;
    font-size: 22px; line-height: 30px; color: var(--brand-blue); white-space: nowrap; }
  .hero-caption strong { font-weight: 700; }
  .slider-dots { position: absolute; left: 568px; top: 468px; display: flex; gap: 7px; }
  .slider-dots span { width: 16px; height: 16px; border-radius: 50%; background: var(--white); }
  .slider-dots span.current { background: var(--brand-blue); border: 3px solid var(--white); }

  .services { position: absolute; top: 635px; left: 0; width: 1200px; }
  .service { position: absolute; width: 170px; }
  .service h2 { height: 24px; background: var(--brand-blue); color: var(--white); font-size: 11.3px;
    font-weight: 600; text-align: center; line-height: 24px; white-space: nowrap; }
  .service-photo { width: 170px; height: 120px; }
  .service-more { position: absolute; left: 145px; top: 118px; width: 29px; height: 29px;
    background: var(--white); padding: 2px; }
  .service-more span { display: flex; width: 25px; height: 25px; background: var(--brand-blue);
    align-items: center; justify-content: center; }
  .service p { margin-top: 24px; font-size: 11.3px; line-height: 18.8px; color: var(--text-dark); width: 176px; }

  .slogan { position: absolute; left: 232px; top: 912px; font-size: 20px; line-height: 25px; color: var(--brand-blue); }

  .site-footer { position: absolute; left: 0; top: 993px; width: 1200px; height: 50px; background: var(--footer-bg);
    color: var(--white); font-size: 9px; letter-spacing: 2.4px; padding: 13px 0 0 232px; }
</style>
</head>
<body>
  <header class="site-header">
    <div class="brand"><span class="brand-mark"></span><span class="brand-name">KERN</span></div>
    <div class="tagline">Ihr Partner für mobile Container</div>
    <nav class="main-nav">
      <a class="active" style="left:0">HOME</a>
      <a style="left:57px">LEISTUNGEN</a>
      <a style="left:143px">WIR ÜBER UNS</a>
      <a style="left:242px">REFERENZEN</a>
      <a style="left:329px">AKTUELLES</a>
      <a style="left:407px">KONTAKT</a>
    </nav>
  </header>

  <section class="hero">
    <div class="hero-photo" role="img" aria-label="Foto einer zweistöckigen weißen Containeranlage mit Außentreppen vor Bäumen und blauem Himmel"></div>
    <div class="hero-caption"><strong>KERN Montagearbeiten</strong> – maßgeschneiderte<br>Lösungen für temporäre Containeranlagen.</div>
    <div class="slider-dots"><span class="current"></span><span></span><span></span></div>
  </section>

  <section class="services">
    <article class="service" style="left:232px">
      <h2>MONTAGE</h2>
      <div class="service-photo" role="img" aria-label="Foto einer Containermontage mit Kran" style="background:linear-gradient(180deg,#c8d8ea 0%,#e6e9ea 40%,#4d6a3a 60%,#3a3f4a 100%)"></div>
      <a class="service-more"><span><svg width="10" height="10" viewBox="0 0 10 10"><path d="M1 1l4 4-4 4M5 1l4 4-4 4" fill="none" stroke="#fff" stroke-width="1.3"/></svg></span></a>
      <p>Ihr mobiles Wunschobjekt stel-<br>len wir aus Containermodulen<br>zusammen und montieren es<br>direkt vor Ort genau nach Maß.</p>
    </article>
    <article class="service" style="left:420px">
      <h2>UMBAU UND VERSETZUNG</h2>
      <div class="service-photo" role="img" aria-label="Foto eines Containerdachs am Kranhaken mit Anschlagseilen" style="background:linear-gradient(180deg,#8fb0dc 0%,#c9d6e8 55%,#6d6f73 85%,#4c4e52 100%)"></div>
      <a class="service-more"><span><svg width="10" height="10" viewBox="0 0 10 10"><path d="M1 1l4 4-4 4M5 1l4 4-4 4" fill="none" stroke="#fff" stroke-width="1.3"/></svg></span></a>
      <p>Egal, ob Sie nur einen kleinen<br>Umbau planen oder<br>Ihr Containerbau an einen<br>neuen Standort wechseln soll –<br>wir kümmern uns um alles!</p>
    </article>
    <article class="service" style="left:609px">
      <h2>REPERATUR</h2>
      <div class="service-photo" role="img" aria-label="Foto einer Innenraumdecke mit Deckenplatten und Leuchten" style="background:linear-gradient(180deg,#d8dadb 0%,#eeeeec 55%,#e7dfc4 100%)"></div>
      <a class="service-more"><span><svg width="10" height="10" viewBox="0 0 10 10"><path d="M1 1l4 4-4 4M5 1l4 4-4 4" fill="none" stroke="#fff" stroke-width="1.3"/></svg></span></a>
      <p>Ist etwas defekt, reparieren wir<br>selbstverständlich Ihr<br>Bauobjekt – kostenbewusst und<br>mit dem nötigen Know-how!</p>
    </article>
    <article class="service" style="left:798px">
      <h2>EINLAGERUNG</h2>
      <div class="service-photo" role="img" aria-label="Foto einer grauen zweistöckigen Containeranlage im Lager" style="background:linear-gradient(180deg,#e4e8ec 0%,#a9acb0 45%,#9a9c9e 78%,#b5b2aa 100%)"></div>
      <a class="service-more"><span><svg width="10" height="10" viewBox="0 0 10 10"><path d="M1 1l4 4-4 4M5 1l4 4-4 4" fill="none" stroke="#fff" stroke-width="1.3"/></svg></span></a>
      <p>Ihr Container kommt gerade<br>nicht zum Einsatz? Dann darf er<br>sich in unserem Zwischenlager<br>ausruhen.</p>
    </article>
  </section>

  <p class="slogan">Wir schaffen mobilen Raum.<br>Profitieren Sie von unserer langjährigen Erfahrung!</p>

  <footer class="site-footer">KERN MONTAGEARBEITEN &nbsp; | © 2017 &nbsp; | &nbsp; IMPRESSUM</footer>
</body>
</html>
```